Commercial Loan Originator Business Card (CHANGE COLORS SCHEME)

CHANGE COLOR SCHEME - SAME DESIGN

Name Miranda Lestock
Title Commercial Loan Originator
Office (800) 641-2905 x68
Direct (240) 731-2264
Email gardenpath4life@mailbox.example

Name Dale Fenwick
Office (800) 641-2905 x70
Direct (410) 392-6058
Email d.fenwickhomes@mailbox.example

Name Gerald Winslow
Office (800) 641-2905 x71
Direct (215) 946-3021
Email g.winslow63@mailbox.example

Name Joan Mallory
Office (800) 641-2905 x
Direct (202) 518-4467
Email jmallory74@mailbox.example

Name Norah Velasco
Office (800) 641-2905 x72
Direct (240) 867-1152
Email capitalhomelending@mailbox.example

```html
<!DOCTYPE html>
<html lang="en">
<head>
<meta charset="utf-8">
<title>Commercial Loan Originator Business Cards</title>
<link href="https://fonts.googleapis.com/css2?family=Arimo:wght@400;700&display=swap" rel="stylesheet">
<style>
  :root {
    --canvas: #666666;
    --charcoal: #2d2d30;
    --orange: #fc840e;
    --yellow: #ffcc00;
    --cream: #ffffcc;
    --white: #ffffff;
    --ring-light: #e6e6e6;
  }
  * { margin: 0; padding: 0; box-sizing: border-box; }
  html, body { width: 1200px; height: 1200px; overflow: hidden; background: var(--canvas); }
  body { position: relative; font-family: "Arimo", Arial, sans-serif; }

  .card {
    position: absolute; width: 472px; height: 268px;
    background: var(--bg); overflow: hidden;
  }
  .card-shadow {
    position: absolute; width: 440px; height: 18px;
    background: radial-gradient(ellipse at center, rgba(0,0,0,.35) 0%, rgba(0,0,0,0) 70%);
  }
  .corner-square { position: absolute; right: 0; top: 0; width: 52px; height: 50px; background: var(--square); }
  .base-block { position: absolute; left: 0; top: 200px; width: 56px; height: 68px; background: var(--base); }
  .base-band { position: absolute; left: 0; top: 245px; width: 100%; height: 23px; background: var(--base); }
  .dots { position: absolute; }
  .dots-top { left: 28px; top: 27px; color: var(--dot-top); }
  .dots-bottom { left: 344px; top: 200px; color: var(--dot-bottom); }

  .portrait {
    position: absolute; left: 46px; top: 58px; width: 124px; height: 124px; border-radius: 50%;
    border: 4px solid var(--ring);
    background: radial-gradient(circle at 50% 40%, var(--photo-a), var(--photo-b));
  }
  .portrait.low { top: 68px; }

  .details { position: absolute; left: 190px; top: 0; width: 280px; height: 100%; }
  .name {
    position: absolute; top: 63px; font-size: 20px; font-weight: 700; letter-spacing: .8px;
    text-transform: uppercase; color: var(--name); white-space: nowrap;
  }
  .title {
    position: absolute; top: 89px; font-size: 9.4px; letter-spacing: .9px;
    text-transform: uppercase; color: var(--title); white-space: nowrap;
  }
  .contact {
    position: absolute; display: flex; align-items: center; gap: 5px;
    font-size: 17.5px; color: var(--text); white-space: nowrap;
  }
  .contact svg { flex: none; color: var(--icon); }
  .contact.office { top: 111px; }
  .contact.direct { top: 139px; }
  .contact.email { top: 164px; font-size: 15px; letter-spacing: -.1px; }

  .theme-charcoal { --bg: var(--charcoal); --square: var(--orange); --base: var(--orange); --dot-top: var(--orange); --dot-bottom: var(--orange);
    --name: var(--orange); --title: var(--white); --text: var(--white); --icon: var(--orange); --ring: var(--ring-light); --photo-a: #e79ab8; --photo-b: #7a4d3c; }
  .theme-orange { --bg: var(--orange); --square: var(--charcoal); --base: var(--charcoal); --dot-top: var(--white); --dot-bottom: var(--charcoal);
    --name: var(--charcoal); --title: var(--charcoal); --text: var(--white); --icon: var(--charcoal); --ring: var(--ring-light); --photo-a: #6f7f95; --photo-b: #222a38; }
  .theme-yellow { --bg: var(--yellow); --square: var(--charcoal); --base: var(--charcoal); --dot-top: var(--charcoal); --dot-bottom: var(--charcoal);
    --name: var(--charcoal); --title: var(--charcoal); --text: var(--charcoal); --icon: var(--charcoal); --ring: var(--charcoal); --photo-a: #b68a72; --photo-b: #4d5a3a; }
  .theme-cream { --bg: var(--cream); --square: var(--charcoal); --base: var(--charcoal); --dot-top: var(--orange); --dot-bottom: var(--orange);
    --name: var(--charcoal); --title: var(--charcoal); --text: var(--charcoal); --icon: var(--charcoal); --ring: var(--orange); --photo-a: #8e6048; --photo-b: #3a2a24; }
  .theme-white { --bg: var(--white); --square: var(--orange); --base: var(--charcoal); --dot-top: var(--orange); --dot-bottom: var(--orange);
    --name: var(--charcoal); --title: var(--charcoal); --text: var(--charcoal); --icon: var(--orange); --ring: var(--orange); --photo-a: #9aa0a6; --photo-b: #3d4236; }
</style>
</head>
<body>

<svg width="0" height="0" style="position:absolute">
  <defs>
    <g id="dot-grid-top" fill="currentColor">
      <rect x="0" y="0" width="8" height="8"/><rect x="28" y="0" width="8" height="8"/><rect x="56" y="0" width="8" height="8"/><rect x="84" y="0" width="8" height="8"/>
      <rect x="0" y="22" width="8" height="8"/><rect x="28" y="22" width="8" height="8"/><rect x="56" y="22" width="8" height="8"/><rect x="84" y="22" width="8" height="8"/>
      <rect x="0" y="44" width="8" height="8"/><rect x="28" y="44" width="8" height="8"/><rect x="56" y="44" width="8" height="8"/><rect x="84" y="44" width="8" height="8"/>
      <rect x="0" y="66" width="8" height="8"/><rect x="28" y="66" width="8" height="8"/>
    </g>
    <g id="dot-grid-bottom" fill="currentColor">
      <rect x="0" y="0" width="8" height="8"/><rect x="28" y="0" width="8" height="8"/><rect x="56" y="0" width="8" height="8"/><rect x="84" y="0" width="8" height="8"/>
      <rect x="0" y="22" width="8" height="8"/><rect x="28" y="22" width="8" height="8"/><rect x="56" y="22" width="8" height="8"/><rect x="84" y="22" width="8" height="8"/>
    </g>
    <symbol id="icon-phone" viewBox="0 0 12 12"><path fill="currentColor" d="M2.6 1l1.8 2.3-1 1.1c.7 1.6 2 2.9 3.5 3.6l1.1-1L10.3 8.7 9.3 10.6C5 10.2 1.6 6.8 1.2 2.5z"/></symbol>
    <symbol id="icon-mobile" viewBox="0 0 12 12"><rect x="3" y="1" width="6" height="10" rx="1" fill="none" stroke="currentColor" stroke-width="1.2"/></symbol>
    <symbol id="icon-mail" viewBox="0 0 12 12"><rect x="1.5" y="3" width="9" height="6" fill="none" stroke="currentColor" stroke-width="1"/><path d="M1.5 3l4.5 3.5L10.5 3" fill="none" stroke="currentColor" stroke-width="1"/></symbol>
  </defs>
</svg>

<!-- Miranda Lestock -->
<div class="card-shadow" style="left:120px; top:404px"></div>
<section class="card theme-charcoal" style="left:104px; top:140px">
  <div class="corner-square"></div><div class="base-block"></div><div class="base-band"></div>
  <svg class="dots dots-top" width="92" height="74"><use href="#dot-grid-top"/></svg>
  <svg class="dots dots-bottom" width="92" height="30"><use href="#dot-grid-bottom"/></svg>
  <div class="portrait" role="img" aria-label="Portrait photo of Miranda Lestock"></div>
  <div class="details">
    <h2 class="name">Miranda Lestock</h2>
    <p class="title">Commercial Loan Originator</p>
    <p class="contact office"><svg width="11" height="11"><use href="#icon-phone"/></svg>(800) 641-2905 x68</p>
    <p class="contact direct"><svg width="11" height="13"><use href="#icon-mobile"/></svg>(240) 731-2264</p>
    <p class="contact email"><svg width="11" height="11"><use href="#icon-mail"/></svg>gardenpath4life@mailbox.example</p>
  </div>
</section>

<!-- Gerald Winslow -->
<div class="card-shadow" style="left:640px; top:404px"></div>
<section class="card theme-orange" style="left:624px; top:140px">
  <div class="corner-square"></div><div class="base-block"></div><div class="base-band"></div>
  <svg class="dots dots-top" width="92" height="74"><use href="#dot-grid-top"/></svg>
  <svg class="dots dots-bottom" width="92" height="30"><use href="#dot-grid-bottom"/></svg>
  <div class="portrait" role="img" aria-label="Portrait photo of Gerald Winslow"></div>
  <div class="details">
    <h2 class="name">Gerald Winslow</h2>
    <p class="title">Commercial Loan Originator</p>
    <p class="contact office"><svg width="11" height="11"><use href="#icon-phone"/></svg>(800) 641-2905 x71</p>
    <p class="contact direct"><svg width="11" height="13"><use href="#icon-mobile"/></svg>(215) 946-3021</p>
    <p class="contact email"><svg width="11" height="11"><use href="#icon-mail"/></svg>g.winslow63@mailbox.example</p>
  </div>
</section>

<!-- Joan Mallory -->
<div class="card-shadow" style="left:122px; top:724px"></div>
<section class="card theme-yellow" style="left:106px; top:460px">
  <div class="corner-square"></div><div class="base-block"></div><div class="base-band"></div>
  <svg class="dots dots-top" width="92" height="74"><use href="#dot-grid-top"/></svg>
  <svg class="dots dots-bottom" width="92" height="30"><use href="#dot-grid-bottom"/></svg>
  <div class="portrait low" role="img" aria-label="Portrait photo of Joan Mallory"></div>
  <div class="details">
    <h2 class="name">Joan Mallory</h2>
    <p class="title">Commercial Loan Originator</p>
    <p class="contact office"><svg width="11" height="11"><use href="#icon-phone"/></svg>(800) 641-2905 x71</p>
    <p class="contact direct"><svg width="11" height="13"><use href="#icon-mobile"/></svg>(202) 518-4467</p>
    <p class="contact email"><svg width="11" height="11"><use href="#icon-mail"/></svg>jmallory74@mailbox.example</p>
  </div>
</section>

<!-- Norah Velasco -->
<div class="card-shadow" style="left:640px; top:724px"></div>
<section class="card theme-cream" style="left:624px; top:460px">
  <div class="corner-square"></div><div class="base-block"></div><div class="base-band"></div>
  <svg class="dots dots-top" width="92" height="74"><use href="#dot-grid-top"/></svg>
  <svg class="dots dots-bottom" width="92" height="30"><use href="#dot-grid-bottom"/></svg>
  <div class="portrait low" style="left:33px" role="img" aria-label="Portrait photo of Norah Velasco"></div>
  <div class="details" style="left:175px">
    <h2 class="name" style="top:67px">Norah Velasco</h2>
    <p class="title" style="top:93px">Commercial Loan Originator</p>
    <p class="contact office" style="top:114px"><svg width="11" height="11"><use href="#icon-phone"/></svg>(800) 641-2905 x72</p>
    <p class="contact direct" style="top:141px"><svg width="11" height="13"><use href="#icon-mobile"/></svg>(240) 867-1152</p>
    <p class="contact email"><svg width="11" height="11"><use href="#icon-mail"/></svg>capitalhomelending@mailbox.example</p>
  </div>
</section>

<!-- Dale Fenwick -->
<div class="card-shadow" style="left:120px; top:1054px"></div>
<section class="card theme-white" style="left:104px; top:790px">
  <div class="corner-square"></div><div class="base-block"></div><div class="base-band"></div>
  <svg class="dots dots-top" width="92" height="74"><use href="#dot-grid-top"/></svg>
  <svg class="dots dots-bottom" width="92" height="30"><use href="#dot-grid-bottom"/></svg>
  <div class="portrait low" role="img" aria-label="Portrait photo of Dale Fenwick"></div>
  <div class="details">
    <h2 class="name">Dale Fenwick</h2>
    <p class="title">Commercial Loan Originator</p>
    <p class="contact office"><svg width="11" height="11"><use href="#icon-phone"/></svg>(800) 641-2905 x70</p>
    <p class="contact direct"><svg width="11" height="13"><use href="#icon-mobile"/></svg>(410) 392-6058</p>
    <p class="contact email"><svg width="11" height="11"><use href="#icon-mail"/></svg>d.fenwickhomes@mailbox.example</p>
  </div>
</section>

</body>
</html>
```